App Design for quiz app (casual gaming app)

We need an design & logo for our quiz app. Its a simple quiz app, where you pick up a category, answer three questions out of this category. After this an opponent is assigned to your game, and has to answer the same three questions. After this first round is finished, it's the opponents turn to choose a new category and answer three questions out of this category. Now it's your turn to answer the same three questions. With this done, the 2nd round is finished. One game has seven rounds.
Please find attached the balsamiq project. For all of you, do not have balsamiq, please find also the mockups as pdf.
Final delivery should be psd files
Target Market(s)
Casual Games

```html
<!DOCTYPE html>
<html lang="en">
<head>
<meta charset="utf-8">
<title>QuizNest – Home</title>
<link href="https://fonts.googleapis.com/css2?family=Figtree:wght@400;500;600&display=swap" rel="stylesheet">
<style>
  :root {
    --green: #5fba74;
    --green-light: #79c68a;
    --white: #ffffff;
    --ink: #3b3f41;
    --ink-soft: #a3a9a8;
    --mint: #c5e0dc;
    --mint-line: #d6e9e6;
    --card: #eef4f3;
    --card-edge: #c9e2dc;
    --card-text: #6f8883;
    --badge: #f2605c;
    --divider: #ececec;
    --photo-a: #b98a66;
    --photo-b: #6e8a55;
  }
  * { box-sizing: border-box; margin: 0; padding: 0; }
  html, body {
    width: 736px; height: 1200px; overflow: hidden;
    background: var(--white);
    font-family: "Figtree", sans-serif;
    color: var(--ink);
  }
  .screen { position: relative; width: 736px; height: 1200px; }

  .app-bar {
    position: absolute; left: 0; top: 0; width: 736px; height: 155px;
    background: linear-gradient(115deg, var(--green) 0 60%, var(--green-light) 60% 100%);
    color: var(--white);
  }
  .status-bar {
    position: absolute; left: 0; top: 0; width: 100%; height: 48px;
    display: flex; align-items: center; justify-content: space-between;
    padding: 0 22px 0 22px; font-size: 22px; font-weight: 500;
  }
  .status-left, .status-right { display: flex; align-items: center; gap: 8px; width: 200px; }
  .status-right { justify-content: flex-end; }
  .signal { display: flex; gap: 3px; }
  .signal i { width: 10px; height: 10px; border-radius: 50%; border: 1.5px solid var(--white); display: block; }
  .signal i.on { background: var(--white); }
  .battery { width: 44px; height: 18px; border: 2px solid var(--white); border-radius: 4px; padding: 2px; position: relative; }
  .battery::after { content: ""; position: absolute; right: -6px; top: 4px; width: 3px; height: 6px; background: var(--white); border-radius: 0 2px 2px 0; }
  .battery span { display: block; width: 100%; height: 100%; background: var(--white); border-radius: 1px; }

  .menu-button { position: absolute; left: 60px; top: 90px; width: 40px; height: 30px; }
  .app-title {
    position: absolute; left: 0; right: 0; top: 80px; text-align: center;
    font-size: 38px; font-weight: 400; letter-spacing: 0.5px;
  }

  .profile { position: absolute; left: 0; top: 155px; width: 100%; height: 385px; border-bottom: 2px solid var(--divider); text-align: center; }
  .avatar-ring {
    position: absolute; left: 251px; top: 25px; width: 236px; height: 236px; border-radius: 50%;
    background: #e3efec; padding: 8px;
  }
  .avatar-photo { width: 100%; height: 100%; border-radius: 50%; background: radial-gradient(circle at 50% 45%, var(--photo-a) 0 35%, var(--photo-b) 75%); }
  .edit-badge {
    position: absolute; left: 410px; top: 208px; width: 46px; height: 46px; border-radius: 50%;
    background: #d4e7e3; border: 4px solid var(--white); display: flex; align-items: center; justify-content: center;
  }
  .profile-name { position: absolute; left: 0; right: 0; top: 283px; font-size: 35px; font-weight: 600; }
  .profile-status { position: absolute; left: 0; right: 0; top: 325px; font-size: 22px; color: var(--ink-soft); }

  .timeline-line { position: absolute; left: 79px; width: 2px; background: var(--mint-line); }
  .section { position: absolute; left: 40px; display: flex; align-items: center; gap: 27px; font-size: 23px; font-weight: 500; }
  .section-icon {
    position: relative; width: 80px; height: 80px; border-radius: 50%; background: var(--mint);
    display: flex; align-items: center; justify-content: center;
  }
  .count-badge {
    position: absolute; right: -2px; top: -4px; width: 26px; height: 26px; border-radius: 50%;
    background: var(--badge); color: var(--white); font-size: 15px; font-weight: 600;
    display: flex; align-items: center; justify-content: center; border: 2px solid var(--white);
  }

  .game-card {
    position: absolute; left: 117px; width: 583px; height: 76px;
    background: var(--card); border-bottom: 3px solid var(--card-edge); border-radius: 3px;
    display: flex; align-items: center; padding: 0 16px 0 28px;
  }
  .game-card::before {
    content: ""; position: absolute; left: -20px; top: 28px;
    border-right: 20px solid var(--card); border-top: 10px solid transparent; border-bottom: 10px solid transparent;
  }
  .opponent-photo { width: 60px; height: 60px; border-radius: 50%; background: radial-gradient(circle at 50% 45%, #e2a07a 0 30%, #9a4a32 70%); }
  .opponent-name { margin-left: 32px; font-size: 24px; color: var(--card-text); flex: 1; }
  .score { text-align: right; color: var(--card-text); }
  .score-value { font-size: 29px; line-height: 1.1; }
  .score-round { font-size: 15px; color: #9fb3af; }
</style>
</head>
<body>
<main class="screen">
  <header class="app-bar">
    <div class="status-bar">
      <div class="status-left">
        <span class="signal"><i class="on"></i><i class="on"></i><i class="on"></i><i></i><i></i></span>
        <span>NOVA</span>
        <svg width="22" height="16" viewBox="0 0 22 16"><path d="M1 6a14 14 0 0 1 20 0M4.5 9.5a9 9 0 0 1 13 0M8 13a4 4 0 0 1 6 0" fill="none" stroke="#fff" stroke-width="2.4" stroke-linecap="round"/></svg>
      </div>
      <span class="status-time">4:21 PM</span>
      <div class="status-right">
        <svg width="12" height="20" viewBox="0 0 12 20"><path d="M1 5l10 9-5 4V2l5 4-10 9" fill="none" stroke="#fff" stroke-width="1.6" opacity=".7"/></svg>
        <span>100%</span>
        <span class="battery"><span></span></span>
      </div>
    </div>
    <svg class="menu-button" viewBox="0 0 40 30" aria-label="Menu"><path d="M0 2h40M0 15h40M0 28h40" stroke="#fff" stroke-width="3"/></svg>
    <h1 class="app-title">QuizNest</h1>
  </header>

  <section class="profile">
    <div class="avatar-ring"><div class="avatar-photo" role="img" aria-label="Profile photo of the player"></div></div>
    <div class="edit-badge">
      <svg width="20" height="20" viewBox="0 0 20 20"><path d="M3 17l2-6 9-9 4 4-9 9z" fill="#fff"/></svg>
    </div>
    <h2 class="profile-name">Owen Hartley</h2>
    <p class="profile-status">Im here to play and win :)</p>
  </section>

  <div class="timeline-line" style="top:653px;height:256px"></div>
  <div class="timeline-line" style="top:989px;height:48px"></div>

  <div class="section" style="top:573px">
    <div class="section-icon">
      <svg width="32" height="30" viewBox="0 0 32 30"><path d="M9 2h14v8a7 7 0 0 1-14 0zM9 4H3v3a6 6 0 0 0 7 6M23 4h6v3a6 6 0 0 1-7 6M16 17v6M10 27h12v-3H10z" fill="#fff" stroke="#fff" stroke-width="2" stroke-linejoin="round"/></svg>
    </div>
    <span>My Turn</span>
  </div>

  <article class="game-card" style="top:674px">
    <div class="opponent-photo" role="img" aria-label="Opponent photo"></div>
    <span class="opponent-name">Clara</span>
    <div class="score"><div class="score-value">3:1</div><div class="score-round">Round 2</div></div>
  </article>
  <article class="game-card" style="top:775px">
    <div class="opponent-photo" role="img" aria-label="Opponent photo"></div>
    <span class="opponent-name">Clara</span>
    <div class="score"><div class="score-value">3:1</div><div class="score-round">Round 2</div></div>
  </article>

  <div class="section" style="top:909px">
    <div class="section-icon">
      <svg width="24" height="32" viewBox="0 0 24 32"><path d="M2 2h20M2 30h20M4 2c0 10 7 10 7 14S4 20 4 30M20 2c0 10-7 10-7 14s7 4 7 14" fill="none" stroke="#fff" stroke-width="2.5"/><path d="M7 27l5-6 5 6z" fill="#fff"/></svg>
      <span class="count-badge">3</span>
    </div>
    <span>Waiting for a Player</span>
  </div>

  <div class="section" style="top:1037px">
    <div class="section-icon">
      <svg width="30" height="24" viewBox="0 0 30 24"><path d="M3 12l8 8L27 4" fill="none" stroke="#fff" stroke-width="4" stroke-linecap="round" stroke-linejoin="round"/></svg>
    </div>
    <span>Finished Games</span>
  </div>
</main>
</body>
</html>
```